Vorrel Letterhead

Need a fresh looking design. We are a IT service company and I would like some elements of the logo to flow through. I have included the logo as an attachment. I have also included business card design as it might help with the design.

Industry/Entity Type

Business

```html
<!DOCTYPE html>
<html lang="en">
<head>
<meta charset="utf-8">
<title>Vorrel Letterhead</title>
<link rel="stylesheet" href="https://fonts.googleapis.com/css2?family=Josefin+Slab:wght@400;600;700&display=swap">
<style>
  :root {
    --backdrop: #e9e9e9;
    --paper: #ffffff;
    --ink: #2b2b2b;
    --brand-green: #8cc63f;
    --brand-grey: #7d8287;
    --shadow: rgba(0, 0, 0, 0.14);
  }
  * { box-sizing: border-box; margin: 0; padding: 0; }
  html, body {
    width: 1200px;
    height: 822px;
    overflow: hidden;
    background: var(--backdrop);
  }
  .canvas {
    position: relative;
    width: 1200px;
    height: 822px;
    display: flex;
    align-items: center;
    justify-content: center;
  }
  .letterhead {
    position: relative;
    width: 552px;
    height: 780px;
    background: var(--paper);
    box-shadow: 0 6px 22px var(--shadow);
    font-family: "Josefin Slab", serif;
    color: var(--ink);
  }
  .brand {
    position: absolute;
    left: 44px;
    top: 40px;
    display: flex;
    align-items: center;
    gap: 8px;
  }
  .brand-name {
    font-family: "Josefin Slab", serif;
    font-weight: 700;
    font-size: 34px;
    line-height: 1;
    color: var(--brand-green);
  }
  .brand-dot {
    width: 10px;
    height: 10px;
    background: var(--brand-green);
  }
  .header-flow {
    position: absolute;
    top: 0;
    right: 0;
    width: 380px;
    height: 190px;
    background: linear-gradient(200deg,
      rgba(125, 130, 135, 0.55) 0%,
      rgba(140, 198, 63, 0.45) 35%,
      rgba(140, 198, 63, 0.15) 65%,
      rgba(255, 255, 255, 0) 90%);
  }
  .letter-body {
    position: absolute;
    left: 60px;
    right: 60px;
    top: 205px;
    font-size: 12.4px;
    line-height: 1.32;
    text-align: justify;
  }
  .salutation { margin-bottom: 12px; }
  .letter-body p + p { margin-top: 14px; }
  .contact {
    position: absolute;
    left: 0;
    right: 0;
    bottom: 62px;
    text-align: center;
    font-size: 12.4px;
    font-weight: 600;
    line-height: 1.25;
  }
</style>
</head>
<body>
<main class="canvas">
  <article class="letterhead">
    <header>
      <div class="brand">
        <span class="brand-name">Vorrel</span>
        <span class="brand-dot"></span>
      </div>
      <div class="header-flow" role="img" aria-label="Flowing pattern of small green and grey brand shapes sweeping across the top right corner"></div>
    </header>

    <section class="letter-body">
      <p class="salutation">Lorem ipsum dolor sit amet,</p>
      <p>Lorem ipsum dolor sit amet, consectetur adipiscing elit. Donec orci purus, luctus vitae dignissim eu, iaculis sed purus. Vivamus faucibus, ipsum nec aliquet viverra, leo mauris condimentum ligula, sit amet sagittis enim ligula quis arcu. Nam egestas tortor id nisi porttitor mattis. In tortor ante, ultricies in suscipit a, tempus non massa. Vivamus et auctor mi. Fusce vel massa nulla. Phasellus nec eros mauris, et sceleris­que orci. Donec malesuada orci vitae nulla accumsan porta a id massa. Quisque ac­cumsan iaculis magna sit amet fringilla. Maecenas consequat, magna eget tincid­unt semper, odio nibh rutrum mi, id feugiat ante nisi eu risus. Vestibulum nunc orci, rhoncus a placerat in, ultricies in mi. Cras mattis varius eros, vel fringilla nisi suscipit eget.</p>
      <p>Quisque scelerisque sagittis nulla at porttitor. Mauris a justo et tellus interdum tris­tique. Sed id augue vitae urna euismod commodo aliquet a quam. Pellentesque arcu velit, cursus et malesuada ut, consequat et diam. Nullam erat sem, rhoncus id ullamcorper vitae, rhoncus et arcu. In ultricies ultricies nulla, ut rutrum nisi iaculis at. Donec eu magna a metus ornare faucibus. Fusce aliquet faucibus ultricies. Morbi semper, est id tincidunt gravida, sem arcu adipiscing lacus, ac bibendum nulla leo eu purus. Quisque nec diam sed risus consectetur a ccumsan quis quis nibh. Vestibu­lum id purus lorem.</p>
      <p>Vivamus vehicula accumsan lacinia. Aliquam erat volutpat. Pellentesque conse­quat venenatis velit non gravida. Etiam et sem et nulla congue aliquam sed eget augue. Nulla facilisi. Pellentesque habitant morbi tristique senectus et netus et malesuada fames ac turpis egestas. Nulla a elit at sem iaculis congue. Nullam mollis tristique lobortis.</p>
    </section>

    <footer class="contact">
      <p>(912) 555-1234</p>
      <p>yourname@yourwebsite.com</p>
      <p>yourwebsite.com</p>
    </footer>
  </article>
</main>
</body>
</html>
```